Kestrel Builders Business Card Design Project

Clean sharp business card
Ability to write on back of card
Details for the card -
Address: PO Box 5867, Marrowvale, Qld, 4208
ABN: 47 305 961 220
BSA LIC 2650874
Ph: 07 3562 4470
Fax: 07 3562 4475
Email: kestrelbuilders@mailbrook.com.au

```html
<!DOCTYPE html>
<html lang="en">
<head>
<meta charset="utf-8">
<title>Kestrel Builders — Business Cards</title>
<link rel="stylesheet" href="https://fonts.googleapis.com/css2?family=Cinzel:wght@400;700&display=swap">
<style>
  :root {
    --page: #ffffff;
    --card-dark: #231f20;
    --accent: #f7941d;
    --ink: #4d4d4f;
    --ink-light: #a7a9ac;
    --brand: #8a8c8f;
  }
  * { margin: 0; padding: 0; box-sizing: border-box; }
  html, body { width: 1200px; height: 954px; overflow: hidden; background: var(--page); }
  body { position: relative; font-family: "Cinzel", serif; }

  .card { position: absolute; }
  .card--front-light { left: 0; top: 0; width: 770px; height: 490px; background: var(--page); }
  .card--front-dark { left: 0; top: 543px; width: 720px; height: 411px; background: var(--card-dark); }
  .card--back-light { left: 814px; top: 0; width: 366px; height: 380px; background: var(--page); border: 2px solid var(--accent); }
  .card--back-dark { left: 800px; top: 600px; width: 380px; height: 354px; background: var(--card-dark); border: 2px solid var(--accent); }

  .brand {
    position: absolute; left: 0; right: 0;
    display: flex; align-items: center; justify-content: center; gap: 18px;
    font-weight: 700; color: var(--brand); letter-spacing: 0.04em; white-space: nowrap;
  }
  .brand__dot { border-radius: 50%; background: var(--accent); flex: none; }

  .card--front-light .brand { top: 175px; font-size: 62px; }
  .card--front-dark .brand { top: 170px; font-size: 58px; }
  .card--front-light .brand__dot, .card--front-dark .brand__dot { width: 34px; height: 34px; }

  .front-email {
    position: absolute; left: 0; right: 0; text-align: center;
    font-size: 21px; letter-spacing: 0.02em;
  }
  .card--front-light .front-email { top: 316px; color: var(--ink); }
  .card--front-dark .front-email { top: 330px; color: var(--ink-light); }

  .details {
    position: absolute; left: 16px; top: 16px; list-style: none;
    font-size: 21px; line-height: 31px; letter-spacing: 0.01em; white-space: nowrap;
  }
  .details .details__email { font-size: 13px; }
  .card--back-light .details { color: var(--ink); }
  .card--back-dark .details { color: var(--ink-light); top: 20px; }

  .card--back-light .brand { top: 268px; font-size: 24px; gap: 8px; }
  .card--back-dark .brand { top: 275px; font-size: 24px; gap: 8px; }
  .card--back-light .brand__dot, .card--back-dark .brand__dot { width: 14px; height: 14px; }
</style>
</head>
<body>

  <section class="card card--front-light" aria-label="Card front, light">
    <div class="brand"><span class="brand__dot"></span>Kestrel Builders</div>
    <p class="front-email">Email: kestrelbuilders@mailbrook.com.au</p>
  </section>

  <section class="card card--back-light" aria-label="Card back, light">
    <ul class="details">
      <li>Address: PO Box 5867,</li>
      <li>Marrowvale, Qld, 4208</li>
      <li>ABN: 47 305 961 220</li>
      <li>BSA LIC 2650874</li>
      <li>Ph: 07 3562 4470</li>
      <li>Fax: 07 3562 4475</li>
      <li>Email: <span class="details__email">kestrelbuilders@mailbrook.com.au</span></li>
    </ul>
    <div class="brand"><span class="brand__dot"></span>Kestrel Builders</div>
  </section>

  <section class="card card--front-dark" aria-label="Card front, dark">
    <div class="brand"><span class="brand__dot"></span>Kestrel Builders</div>
    <p class="front-email">Email: kestrelbuilders@mailbrook.com.au</p>
  </section>

  <section class="card card--back-dark" aria-label="Card back, dark">
    <ul class="details">
      <li>Address: PO Box 5867,</li>
      <li>Marrowvale, Qld, 4208</li>
      <li>ABN: 47 305 961 220</li>
      <li>BSA LIC 2650874</li>
      <li>Ph: 07 3562 4470</li>
      <li>Fax: 07 3562 4475</li>
      <li>Email: <span class="details__email">kestrelbuilders@mailbrook.com.au</span></li>
    </ul>
    <div class="brand"><span class="brand__dot"></span>Kestrel Builders</div>
  </section>

</body>
</html>
```